Progressive European Honey Business needs minimalistic packaging design

Hello - thank you for your interest in our brief. We are Velvet Jinx, a London based Honey business, importing only the best honey Europe has to offer. Our values are deeply rooted with in progressive liberal values and we are looking for minimalist packaging, which reflects that.

We are looking for a design, which dimensions fit with our packaging option (Kelmor Glass Jar | HEIGHT 90mm | DIAMETER 63mm). We will require a various output files (High Resolution JPEG (CMYK Colors 300 dpi) Source File Ai, PSD, PDF, Printing files (die cut, die folding) and a 3D Mockup of the packaging for use within digital commerce platforms.

We must be able to adjust the free text on the label front and it should include the following:
Brand Name
Honey type
Limited edition No. X / 100 ( X being the number of purchase i.e. 25 / 100)
EU Honey, Single Orgin (Germany)
(c) The net weight (250g)

The back must include room for additional information (again adjustable by us) and the following:
“Unsuitable for children under 12 months”
(b) The appropriate durability declaration

In total, we are looking for
a) A front label
b) A back label
c) A seal (round) including the attached bee and logo included in the Zip file.
Do note that a) & b) can also be combined into one design as long as the symmetry on the jar stays intact.

The final design should communicate modern aesthetics, high quality, that are slightly provocative and pop off the shelves.
Updates

Hi folks, sorry for the delay in completing this project, but my business partner had a leak in his house. We planned to finalise our review today, but this will have to wait until it's no longer raining in his livingroom. Our sincere apologies!

Other font styles liked:
• See branding guidelines

Requirements
Must have
• Must follow the branding guideline and fonts provided as attachment

```html
<!DOCTYPE html>
<html lang="en">
<head>
<meta charset="utf-8">
<title>Velvet Jinx – Front Label</title>
<link href="https://fonts.googleapis.com/css2?family=Josefin+Sans:wght@300;400;700&family=Outfit:wght@400;600;800;900&display=swap" rel="stylesheet">
<style>
  :root {
    --page: #ffffff;
    --label-dark: #2a2a2a;
    --band-white: #f4f4f4;
    --accent-orange: #e8672f;
    --accent-deep: #d95a25;
    --text-light: #f2f2f2;
    --pill-bg: #f7f7f7;
    --pill-text: #2a2a2a;
  }
  * { margin: 0; padding: 0; box-sizing: border-box; }
  html, body {
    width: 1200px;
    height: 750px;
    overflow: hidden;
    background: var(--page);
  }
  .canvas {
    position: relative;
    width: 1200px;
    height: 750px;
    background: var(--page);
  }
  .front-label {
    position: absolute;
    left: 414px;
    top: 118px;
    width: 372px;
    height: 515px;
    background: var(--label-dark);
    color: var(--text-light);
    overflow: hidden;
  }
  .label-graphics {
    position: absolute;
    inset: 0;
  }
  .edition {
    position: absolute;
    top: 35px;
    left: 58px;
    display: flex;
    align-items: center;
    gap: 10px;
  }
  .edition-label {
    font-family: "Josefin Sans", sans-serif;
    font-weight: 400;
    font-size: 11px;
    letter-spacing: 3.2px;
    padding-top: 3px;
  }
  .edition-number {
    font-family: "Outfit", sans-serif;
    font-weight: 600;
    font-size: 11px;
    background: var(--pill-bg);
    color: var(--pill-text);
    border-radius: 13px;
    padding: 6px 9px;
  }
  .brand-name {
    position: absolute;
    top: 138px;
    left: 0;
    width: 100%;
    text-align: center;
    font-family: "Outfit", sans-serif;
    font-weight: 900;
    font-size: 43px;
    line-height: 46px;
    letter-spacing: 0.5px;
    color: var(--accent-orange);
    text-transform: uppercase;
  }
  .honey-type {
    position: absolute;
    top: 268px;
    left: 0;
    width: 100%;
    text-align: center;
    font-family: "Josefin Sans", sans-serif;
    font-weight: 700;
    font-size: 29px;
    letter-spacing: 8px;
    padding-left: 8px;
  }
  .origin {
    position: absolute;
    top: 335px;
    left: 0;
    width: 100%;
    height: 80px;
  }
  .origin-seal {
    position: absolute;
    left: 70px;
    top: 23px;
  }
  .origin-title {
    font-family: "Outfit", sans-serif;
    font-weight: 600;
    font-size: 22px;
    line-height: 22px;
    letter-spacing: -0.3px;
  }
  .origin-sub {
    font-family: "Josefin Sans", sans-serif;
    font-weight: 400;
    font-size: 11px;
    letter-spacing: 2.4px;
    margin-top: 1px;
  }
  .origin-divider {
    position: absolute;
    left: 188px;
    top: 0;
    width: 1.5px;
    height: 80px;
    background: var(--text-light);
  }
  .origin-country {
    position: absolute;
    left: 204px;
    top: 30px;
    font-family: "Outfit", sans-serif;
    font-weight: 400;
    font-size: 21px;
    letter-spacing: 0.5px;
  }
  .net-weight {
    position: absolute;
    top: 445px;
    left: 0;
    width: 100%;
    text-align: center;
  }
  .net-weight-value {
    font-family: "Outfit", sans-serif;
    font-weight: 600;
    font-size: 18px;
    line-height: 20px;
  }
  .net-weight-label {
    font-family: "Josefin Sans", sans-serif;
    font-weight: 400;
    font-size: 9px;
    letter-spacing: 3.5px;
    padding-left: 3px;
    margin-top: 5px;
  }
</style>
</head>
<body>
  <main class="canvas">
    <section class="front-label">
      <svg class="label-graphics" width="372" height="515" viewBox="0 0 372 515" aria-hidden="true">
        <polygon class="band-white" points="0,114 170,102 372,98 372,199 0,202" fill="var(--band-white)"/>
        <polygon class="wedge-top" points="168,102 372,86 372,122" fill="var(--accent-orange)"/>
        <polygon class="wedge-bottom" points="0,201 190,218 0,233" fill="var(--accent-deep)"/>
      </svg>

      <div class="edition">
        <span class="edition-label">LIMITED EDITION NO.</span>
        <span class="edition-number">25/100</span>
      </div>

      <h1 class="brand-name">Velvet Jinx</h1>

      <h2 class="honey-type">HONEY TYPE</h2>

      <div class="origin">
        <div class="origin-seal">
          <div class="origin-title">EU HONEY</div>
          <div class="origin-sub">SINGLE ORIGIN</div>
        </div>
        <div class="origin-divider"></div>
        <div class="origin-country">Germany</div>
      </div>

      <div class="net-weight">
        <div class="net-weight-value">(250g)</div>
        <div class="net-weight-label">NET WEIGHT</div>
      </div>
    </section>
  </main>
</body>
</html>
```